New Coffee Brand Packaging Design

We need a package design for our new coffee brand called Brindle Oak Coffee. Our brand mission will be displayed on the packaging (along the side or the back) and we currently have a logo that should be displayed on the front. Feel free to suggest a new logo design as you are designing the packaging if it doesn't fit with your vision. The final design should be creative and conservative. We like coffee colors (dark and light browns, white, cream, black, gold). We also like chalkboard art imagery (i.e. coffee cups, theme words from our mission, people, etc.). One famous person from West Louisville, KY is Terrence Vogt (world famous boxer and activist). If there is a way to draw his image in more of an abstract way where it doesn't infringe any patents that would be the sort of creativity we would like in the packaging. Our coffee brand prides itself on being a coffee for the people. For the average joe, working American who enjoys a good cup of coffee and a good atmosphere.

Brindle Oak Coffee Mission: "We aim to be a coffee company for the people. The people who have an appreciation and love for family, community and who never forget where they came from. Our coffee was born out of West Louisville, KY…a place like many others where the hearts, the minds and the wills are strong. We hope you enjoy each and every cup. Peace & Blessings."

Requirements
Must have
• (On the side or on the back of the packaging) Brindle Oak Coffee Mission: "We aim to be a coffee company for the people. The people who have an appreciation and love for family, community and who never forget where they came from. Our coffee was born out of West Louisville, KY…a place like many others where the hearts, the minds and the wills are strong. We hope you enjoy each and every cup. Peace & Blessings."
Nice to have
• Coffee Colors: dark and light browns, white, cream, black, gold

```html
<!DOCTYPE html>
<html lang="en">
<head>
<meta charset="utf-8">
<title>Brindle Oak Coffee – Front Panel Options</title>
<link rel="stylesheet" href="https://fonts.googleapis.com/css2?family=Open+Sans:wght@700;800&display=swap">
<style>
  :root {
    --page: #ffffff;
    --roast-dark: #3d1f18;
    --roast-light: #9c7858;
    --ink-dark: #3a1d16;
    --cream: #ffffff;
    --label-plate: #ffffff;
    --art-dark: #5a3a30;
    --art-light: #b89778;
    --caption: #1a1a1a;
  }
  html, body {
    margin: 0;
    padding: 0;
    overflow: hidden;
    background: var(--page);
  }
  .canvas {
    position: relative;
    width: 1200px;
    height: 856px;
    background: var(--page);
    overflow: hidden;
    font-family: "Open Sans", Arial, sans-serif;
  }
  .bag {
    position: absolute;
    top: 100px;
    width: 444px;
    height: 636px;
  }
  .bag--dark { left: 113px; }
  .bag--light { left: 647px; }
  .bag-body--dark { fill: var(--roast-dark); }
  .bag-body--light { fill: var(--roast-light); }
  .label-plate { fill: var(--label-plate); }
  .brand-name {
    font-family: "Open Sans", Arial, sans-serif;
    font-weight: 800;
    font-size: 15px;
    fill: var(--ink-dark);
  }
  .mission {
    font-family: "Open Sans", Arial, sans-serif;
    font-weight: 800;
    fill: var(--cream);
  }
  .mission .accent { fill: var(--ink-dark); }
  .mission .small-word { font-size: 0.7em; }
  .art-area--dark { fill: var(--art-dark); }
  .art-area--light { fill: var(--art-light); }
  .option-caption {
    position: absolute;
    top: 768px;
    margin: 0;
    font-size: 13px;
    font-weight: 800;
    color: var(--caption);
  }
  .option-caption--a { left: 113px; }
  .option-caption--b { left: 636px; }
</style>
</head>
<body>
<main class="canvas">

  <!-- Option A: dark roast bag -->
  <svg class="bag bag--dark" viewBox="0 0 444 636" xmlns="http://www.w3.org/2000/svg">
    <path class="bag-body--dark" d="M0 2 Q0 0 2 0 H442 Q444 0 444 2 L400 612 Q398 636 370 636 H74 Q46 636 44 612 Z"/>
    <rect class="label-plate" x="140" y="57" width="162" height="60"/>
    <text class="brand-name" x="221" y="92" text-anchor="middle">Brindle Oak Coffee</text>

    <g class="mission">
      <text x="68" y="170" font-size="12" textLength="110" lengthAdjust="spacingAndGlyphs">WE AIM TO BE A</text>
      <text x="68" y="196" font-size="31" textLength="310" lengthAdjust="spacingAndGlyphs">COFFEE COMPANY</text>
      <text x="68" y="213" font-size="13" textLength="100" lengthAdjust="spacingAndGlyphs">FOR THE PEOPLE.</text>
      <text x="205" y="213" font-size="13" textLength="172" lengthAdjust="spacingAndGlyphs">THE PEOPLE WHO HAVE</text>
      <text x="68" y="229" font-size="13" textLength="166" lengthAdjust="spacingAndGlyphs">AN APPRECIATION AND</text>
      <text x="68" y="250" font-size="24" textLength="185" lengthAdjust="spacingAndGlyphs">FOR FAMILY,</text>
      <text x="256" y="249" font-size="44" textLength="122" lengthAdjust="spacingAndGlyphs">LOVE</text>
      <text x="68" y="269" font-size="13.5" textLength="308" lengthAdjust="spacingAndGlyphs">COMMUNITY AND WHO NEVER FORGET</text>
      <text x="68" y="290" font-size="21" textLength="302" lengthAdjust="spacingAndGlyphs">WHERE THEY CAME FROM.</text>
      <text x="68" y="313" font-size="12.5" textLength="165" lengthAdjust="spacingAndGlyphs">OUR COFFEE WAS BORN OUT OF</text>
      <text x="68" y="340" font-size="28" textLength="308" lengthAdjust="spacingAndGlyphs">WEST LOUISVILLE, KY</text>
      <text x="68" y="357" font-size="15" textLength="304" lengthAdjust="spacingAndGlyphs">A PLACE LIKE MANY OTHERS WHERE</text>
      <text x="68" y="373" font-size="15" textLength="314" lengthAdjust="spacingAndGlyphs">THE HEARTS, THE MINDS <tspan class="small-word">AND</tspan> THE WILLS</text>
      <text x="68" y="411" font-size="42" textLength="310" lengthAdjust="spacingAndGlyphs">ARE STRONG</text>
      <text x="68" y="428" font-size="12.5" textLength="310" lengthAdjust="spacingAndGlyphs">WE HOPE YOU ENJOY EACH AND EVERY CUP.</text>
      <text x="68" y="455" font-size="28" textLength="305" lengthAdjust="spacingAndGlyphs">PEACE &amp; BLESSINGS</text>
    </g>

    <rect class="art-area--dark" x="72" y="474" width="292" height="100" rx="8"
          role="img" aria-label="Chalk-style illustration of a steaming coffee cup with a heart, flanked by leafy branches, coffee beans and small hearts"/>
  </svg>

  <!-- Option B: light roast bag -->
  <svg class="bag bag--light" viewBox="0 0 444 636" xmlns="http://www.w3.org/2000/svg">
    <path class="bag-body--light" d="M0 2 Q0 0 2 0 H442 Q444 0 444 2 L400 612 Q398 636 370 636 H74 Q46 636 44 612 Z"/>
    <rect class="label-plate" x="140" y="57" width="162" height="60"/>
    <text class="brand-name" x="221" y="92" text-anchor="middle">Brindle Oak Coffee</text>

    <g class="mission">
      <text x="68" y="170" font-size="12" textLength="110" lengthAdjust="spacingAndGlyphs">WE AIM TO BE A</text>
      <text class="accent" x="68" y="196" font-size="31" textLength="310" lengthAdjust="spacingAndGlyphs">COFFEE COMPANY</text>
      <text x="68" y="213" font-size="13" textLength="100" lengthAdjust="spacingAndGlyphs">FOR THE PEOPLE.</text>
      <text x="205" y="213" font-size="13" textLength="172" lengthAdjust="spacingAndGlyphs">THE PEOPLE WHO HAVE</text>
      <text x="68" y="229" font-size="13" textLength="166" lengthAdjust="spacingAndGlyphs">AN APPRECIATION AND</text>
      <text x="68" y="250" font-size="24" textLength="185" lengthAdjust="spacingAndGlyphs">FOR <tspan class="accent">FAMILY,</tspan></text>
      <text class="accent" x="256" y="249" font-size="44" textLength="122" lengthAdjust="spacingAndGlyphs">LOVE</text>
      <text x="68" y="269" font-size="13.5" textLength="308" lengthAdjust="spacingAndGlyphs"><tspan class="accent">COMMUNITY</tspan> AND WHO NEVER FORGET</text>
      <text x="68" y="290" font-size="21" textLength="302" lengthAdjust="spacingAndGlyphs">WHERE THEY CAME FROM.</text>
      <text x="68" y="313" font-size="12.5" textLength="165" lengthAdjust="spacingAndGlyphs">OUR COFFEE WAS BORN OUT OF</text>
      <text x="68" y="340" font-size="28" textLength="308" lengthAdjust="spacingAndGlyphs">WEST LOUISVILLE, KY</text>
      <text x="68" y="357" font-size="15" textLength="304" lengthAdjust="spacingAndGlyphs">A PLACE LIKE MANY OTHERS WHERE</text>
      <text x="68" y="373" font-size="15" textLength="314" lengthAdjust="spacingAndGlyphs">THE HEARTS, THE MINDS <tspan class="small-word">AND</tspan> THE WILLS</text>
      <text x="68" y="411" font-size="42" textLength="310" lengthAdjust="spacingAndGlyphs">ARE <tspan class="accent">STRONG</tspan></text>
      <text x="68" y="428" font-size="12.5" textLength="310" lengthAdjust="spacingAndGlyphs">WE HOPE YOU ENJOY EACH AND EVERY CUP.</text>
      <text x="68" y="455" font-size="28" textLength="305" lengthAdjust="spacingAndGlyphs">PEACE &amp; BLESSINGS</text>
    </g>

    <rect class="art-area--light" x="72" y="474" width="292" height="100" rx="8"
          role="img" aria-label="Chalk-style illustration of a dark steaming coffee cup with a heart, flanked by white leafy branches, coffee beans and small hearts"/>
  </svg>

  <p class="option-caption option-caption--a">front 3A</p>
  <p class="option-caption option-caption--b">front3B</p>

</main>
</body>
</html>
```